Cat sitting business Web Design Project ***

I have a cat sitting business where I either take care of cats in their home or board them in mine

I need a website which offers my services, my rates, about me, FAQ's, Hours of operation and service areas covered, testimonials, contact info, newsletter sign up, gallery of photos and the ability for me to go in and update when needed.

Coding

Coded - Design and coding required

Number of Pages Required

5+ page

```html
<!DOCTYPE html>
<html lang="en">
<head>
<meta charset="utf-8">
<title>Honey Paws Cat Sitting</title>
<link href="https://fonts.googleapis.com/css2?family=Nunito:wght@400;500;600;700;800&display=swap" rel="stylesheet">
<style>
:root{
  --green:#8cc152;
  --green-dark:#7ab342;
  --ink:#1f1f1f;
  --text:#555;
  --muted:#8a8a8a;
  --line:#e3e3e3;
  --band:#f4f4f4;
  --accent:#b5534f;
  --white:#fff;
}
*{box-sizing:border-box;margin:0;padding:0}
html,body{width:1200px;height:4796px;overflow:hidden;background:var(--white)}
body{font-family:"Nunito",sans-serif;color:var(--ink);position:relative}
.abs{position:absolute}
a{color:inherit;text-decoration:none}
.eyebrow{color:var(--green);font-size:22px;font-weight:500}
.section-title{font-size:39px;font-weight:600;color:var(--ink)}
.center{text-align:center;left:0;width:1200px}
.body-text{font-size:13px;line-height:21px;color:var(--text)}

/* header */
.brand{left:86px;top:30px;width:140px;text-align:center}
.brand-mark{width:74px;height:74px;border-radius:50%;border:2px solid var(--green);margin:0 auto 6px}
.brand-name{font-size:20px;font-weight:600;color:var(--accent);line-height:22px}
.nav{left:261px;top:31px;display:flex;gap:33px;font-size:14px;font-weight:500}
.nav a.active{color:var(--green)}
.btn{display:inline-flex;align-items:center;justify-content:center;border-radius:40px;font-size:13px;font-weight:600}
.btn-solid{background:var(--green);color:var(--white)}
.nav-cta{left:951px;top:18px;width:162px;height:48px}

/* hero */
.hero-title{left:86px;top:220px;font-size:54px;line-height:63px;font-weight:700;color:var(--green);width:520px}
.hero-text{left:86px;top:428px;width:410px}
.hero-cta{left:86px;top:513px;width:165px;height:50px;border:2px solid var(--green);color:var(--green);justify-content:flex-start;padding-left:24px}
.hero-cta .arrow{position:absolute;right:-2px;top:-2px;width:50px;height:50px;border-radius:50%;background:var(--green);display:flex;align-items:center;justify-content:center}
.hero-phone{left:274px;top:526px;display:flex;align-items:center;gap:14px;font-size:13px;font-weight:700}
.photo-tall{left:655px;top:130px;width:286px;height:517px;border-radius:143px;background:linear-gradient(160deg,#c9c9c6,#8d8c88 60%,#d9d8d4)}
.photo-side{left:986px;top:205px;width:260px;height:353px;border-radius:130px;background:linear-gradient(150deg,#f2b77a,#d98745 60%,#f6d3a8)}
.divider{left:86px;top:722px;width:1028px;height:1px;background:var(--line)}

/* about */
.about-photos{left:344px;top:1010px;display:flex;gap:10px}
.about-photos div{width:160px;height:112px;border-radius:6px}
.about-btn{left:519px;top:1161px;width:162px;height:48px}

/* services */
.band{left:0;top:1311px;width:1200px;height:503px;background:var(--band)}
.services-intro{left:86px;top:1405px;width:290px}
.services-intro h2{font-size:39px;line-height:46px;font-weight:600;margin:12px 0 20px}
.card{width:237px;height:301px;background:var(--white);border-radius:14px;top:1412px;text-align:center;padding-top:30px;box-shadow:0 2px 10px rgba(0,0,0,.04)}
.card .icon{width:50px;height:50px;border-radius:50%;border:2px solid var(--accent);margin:0 auto 22px}
.card h3{font-size:22px;font-weight:500;margin-bottom:14px}
.card p{font-size:13px;line-height:21px;color:var(--text);width:185px;margin:0 auto 26px}
.card .num{width:46px;height:46px;border-radius:50%;background:var(--green);color:var(--white);font-weight:700;font-size:20px;display:flex;align-items:center;justify-content:center;margin:0 auto}

/* faq */
.faq-item{left:86px;width:1028px;border:1px solid #ececec;border-radius:6px;box-shadow:0 2px 8px rgba(0,0,0,.04);padding:0 28px}
.faq-q{height:56px;display:flex;align-items:center;justify-content:space-between;font-size:17px;font-weight:600}
.faq-item.open .faq-q{color:var(--green);height:78px}
.faq-a{font-size:12px;line-height:23px;color:var(--text);padding-bottom:20px}

/* pricing */
.pricing-intro{left:86px;top:2523px;width:130px}
.pricing-intro h2{font-size:39px;line-height:52px;font-weight:600;margin-bottom:22px}
.plan{top:2533px;height:527px;background:var(--white);border-radius:16px;box-shadow:0 4px 18px rgba(0,0,0,.06);text-align:center;padding-top:44px}
.plan.featured{top:2507px;height:581px;background:var(--green);color:var(--white);padding-top:70px;z-index:2}
.plan h3{font-size:25px;font-weight:700}
.plan .icon{width:64px;height:64px;border-radius:50%;border:2px solid var(--green);margin:22px auto 30px}
.plan.featured .icon{border-color:var(--white)}
.plan ul{list-style:none;width:180px;margin:0 auto}
.plan li{display:flex;justify-content:space-between;align-items:center;font-size:12px;height:35px;color:var(--text)}
.plan.featured li{color:#e9f5dc}
.plan li span{flex:1;text-align:center}
.price{margin-top:20px;font-size:42px;font-weight:800;color:var(--green)}
.price small{font-size:15px;font-weight:500}
.plan.featured .price{color:var(--white)}

/* gallery */
.gallery{left:0;top:3186px;display:flex}
.gallery div{width:240px;height:255px}

/* testimonials */
.avatar{left:546px;top:3646px;width:107px;height:107px;border-radius:50%;background:linear-gradient(140deg,#b58a6d,#6a4a3a)}
.dots{left:0;width:1200px;top:3940px;display:flex;justify-content:center;gap:24px;align-items:center}
.dots i{width:10px;height:10px;border-radius:50%;background:#ccc}
.dots i.on{width:18px;height:18px;background:var(--accent)}

/* newsletter */
.newsletter{left:86px;top:4062px;width:1028px;height:257px;border-radius:129px;background:var(--green)}
.newsletter h2{position:absolute;left:70px;top:100px;font-size:39px;font-weight:700;color:var(--ink)}
.newsletter p{position:absolute;left:70px;top:154px;font-size:13px;color:#3f6f1e}
.news-input{position:absolute;left:517px;top:97px;width:440px;height:67px;background:var(--white);border-radius:34px;font-size:12px;color:var(--muted);padding-left:32px;display:flex;align-items:center}
.news-input .go{position:absolute;right:0;top:0;width:67px;height:67px;border-radius:50%;background:var(--accent);display:flex;align-items:center;justify-content:center}

/* footer */
.foot-brand{left:86px;top:4480px;width:160px;text-align:center}
.foot-col h4{font-size:20px;font-weight:500;color:var(--green);margin-bottom:22px}
.foot-col li{list-style:none;font-size:13px;color:var(--text);display:flex;align-items:center;gap:14px;height:40px}
.foot-col p{font-size:13px;line-height:25px;color:var(--text)}
.bottom{left:86px;top:4733px;width:1028px;display:flex;justify-content:space-between;font-size:12px;font-weight:600}
.social{display:flex;gap:14px;font-weight:800;font-size:13px;color:#2d3a5a}
</style>
</head>
<body>

<header>
  <div class="abs brand"><div class="brand-mark"></div><div class="brand-name">Honey Paws<br>Cat Sitting</div></div>
  <nav class="abs nav"><a class="active" href="#">Home</a><a href="#">About</a><a href="#">My Services</a><a href="#">Pricing</a><a href="#">FAQs</a><a href="#">Testimonials</a><a href="#">Gallery</a><a href="#">Contact</a></nav>
  <a class="abs btn btn-solid nav-cta" href="#">Contact Me</a>
</header>

<section class="hero">
  <h1 class="abs hero-title">Cats make the rule, I just try to follow them</h1>
  <p class="abs hero-text body-text">There are many variations of passages of Lorem Ipsum available, but there majority have suffered alteration in some form, by injected humour,</p>
  <a class="abs btn hero-cta" href="#">Contact Me<span class="arrow"><svg width="18" height="18" viewBox="0 0 18 18"><path d="M4 14L14 4M6 4h8v8" stroke="#fff" stroke-width="1.8" fill="none"/></svg></span></a>
  <div class="abs hero-phone"><svg width="22" height="22" viewBox="0 0 24 24"><path d="M5 3h4l2 5-2.5 1.5a11 11 0 0 0 6 6L16 13l5 2v4a2 2 0 0 1-2 2A16 16 0 0 1 3 5a2 2 0 0 1 2-2z" fill="none" stroke="var(--accent)" stroke-width="1.6"/></svg>415-555-0192</div>
  <div class="abs photo-tall" role="img" aria-label="Grey tabby kitten looking up"></div>
  <div class="abs photo-side" role="img" aria-label="Ginger kitten lying down"></div>
  <div class="abs divider"></div>
</section>

<section class="about">
  <p class="abs eyebrow center" style="top:818px">About Me</p>
  <h2 class="abs section-title center" style="top:858px">I will make them truely happy</h2>
  <p class="abs body-text center" style="top:918px;left:225px;width:750px">Lorem ipsum dolor sit amet, consectetur adipiscing elit. Quisque non nulla eu elit maximus tempus molestie sit amet libero. Sed erat massa, ornare ac orci ut, faucibus convallis turpis. Sed aliquam, lorem ut faucibus placerat, magna sapien convallis tellus, sit amet consequat ante sem vel urna.</p>
  <div class="abs about-photos">
    <div role="img" aria-label="Woman cuddling a cat" style="background:linear-gradient(135deg,#d8b89a,#6b4a38)"></div>
    <div role="img" aria-label="Woman holding a tabby cat" style="background:linear-gradient(135deg,#cfc2b4,#7c6a5c)"></div>
    <div role="img" aria-label="Person relaxing with a cat" style="background:linear-gradient(135deg,#9aa3b5,#5a4e48)"></div>
  </div>
  <a class="abs btn btn-solid about-btn" href="#">Discover More</a>
</section>

<section class="services">
  <div class="abs band"></div>
  <div class="abs services-intro">
    <p class="eyebrow">My Services</p>
    <h2>How I can help you properly.</h2>
    <p class="body-text">There are many variations of passages of Lorem Ipsum available, but there majority have suffered alteration in some form, by injected humour</p>
  </div>
  <article class="abs card" style="left:394px"><div class="icon" role="img" aria-label="Cat care icon"></div><h3>Service One</h3><p>Nulla Lorem mollit cupidatat irure. Laborum magna nulla duis ullamco cillum dolo</p><div class="num">1</div></article>
  <article class="abs card" style="left:658px"><div class="icon" role="img" aria-label="Litter box icon"></div><h3>Service Two</h3><p>Nulla Lorem mollit cupidatat irure. Laborum magna nulla duis ullamco cillum dolo</p><div class="num">2</div></article>
  <article class="abs card" style="left:921px"><div class="icon" role="img" aria-label="Paw heart icon"></div><h3>Service Three</h3><p>Nulla Lorem mollit cupidatat irure. Laborum magna nulla duis ullamco cillum dolo</p><div class="num">3</div></article>
  <article class="abs card" style="left:1184px"></article>
</section>

<section class="faq">
  <p class="abs eyebrow center" style="top:1910px">Frequently Asked Questions</p>
  <h2 class="abs section-title center" style="top:1948px">I am working for the community.</h2>
  <div class="abs faq-item open" style="top:2027px;height:153px">
    <div class="faq-q">01. Lorem Ipsum is simply dummy text?<svg width="18" height="18"><path d="M1 9h16" stroke="var(--green)" stroke-width="2"/></svg></div>
    <p class="faq-a">The tone and elucidates the of system the universal village piink like so to her a try eye. of notice his a associates, could but a listen. Then these and, to small, what's to language. snow doing versus as and if uninspired, clock, up name the joke.</p>
  </div>
  <div class="abs faq-item" style="top:2198px"><div class="faq-q">02. Lorem Ipsum is dummy text?<svg width="18" height="18"><path d="M1 9h16M9 1v16" stroke="var(--green)" stroke-width="2"/></svg></div></div>
  <div class="abs faq-item" style="top:2273px"><div class="faq-q">03. Lorem Ipsum is text?<svg width="18" height="18"><path d="M1 9h16M9 1v16" stroke="var(--green)" stroke-width="2"/></svg></div></div>
  <div class="abs faq-item" style="top:2349px"><div class="faq-q">04. Lorem Ipsum is simply dummy text?<svg width="18" height="18"><path d="M1 9h16M9 1v16" stroke="var(--green)" stroke-width="2"/></svg></div></div>
</section>

<svg width="0" height="0" style="position:absolute">
  <defs>
    <symbol id="tick" viewBox="0 0 14 14"><path d="M2 7l3.5 3.5L12 3" fill="none" stroke="currentColor" stroke-width="1.6"/></symbol>
    <symbol id="cross" viewBox="0 0 14 14"><path d="M3 3l8 8M11 3l-8 8" fill="none" stroke="currentColor" stroke-width="1.6"/></symbol>
  </defs>
</svg>

<section class="pricing">
  <div class="abs pricing-intro"><h2>My Pricing</h2><p class="body-text">There are many variations of passages of Lorem Ipsum available, but there majority have suffered alteration in some form, by injected humour</p></div>
  <article class="abs plan" style="left:249px;width:289px">
    <h3>Regular Session</h3><div class="icon" role="img" aria-label="Cat line icon"></div>
    <ul style="color:var(--accent)">
      <li><span>Pet Shower</span><svg width="14" height="14"><use href="#tick"/></svg></li>
      <li><span>Fitness Checkup</span><svg width="14" height="14"><use href="#tick"/></svg></li>
      <li><span>Pet Grooming</span><svg width="14" height="14"><use href="#tick"/></svg></li>
      <li><span>Hair And Nail Cut</span><svg width="14" height="14"><use href="#tick"/></svg></li>
      <li><span>Control Hair Falling</span><svg width="14" height="14" style="color:var(--green)"><use href="#cross"/></svg></li>
      <li><span>Brush &amp; Blow Dry</span><svg width="14" height="14" style="color:var(--green)"><use href="#cross"/></svg></li>
      <li><span>Pet Park And Games</span><svg width="14" height="14" style="color:var(--green)"><use href="#cross"/></svg></li>
    </ul>
    <p class="price">$99 <small>/ Per Session</small></p>
  </article>
  <article class="abs plan featured" style="left:532px;width:296px">
    <h3>Exclusive Session</h3><div class="icon" role="img" aria-label="Cat line icon"></div>
    <ul style="color:#e6f3d6">
      <li><span>Pet Shower</span><svg width="14" height="14"><use href="#tick"/></svg></li>
      <li><span>Fitness Checkup</span><svg width="14" height="14"><use href="#tick"/></svg></li>
      <li><span>Pet Grooming</span><svg width="14" height="14"><use href="#tick"/></svg></li>
      <li><span>Hair And Nail Cut</span><svg width="14" height="14"><use href="#tick"/></svg></li>
      <li><span>Control Hair Falling</span><svg width="14" height="14"><use href="#tick"/></svg></li>
      <li><span>Brush &amp; Blow Dry</span><svg width="14" height="14" style="color:var(--ink)"><use href="#cross"/></svg></li>
      <li><span>Pet Park And Games</span><svg width="14" height="14" style="color:var(--ink)"><use href="#cross"/></svg></li>
    </ul>
    <p class="price">$130 <small>/ Per Session</small></p>
  </article>
  <article class="abs plan" style="left:828px;width:286px">
    <h3>Premium Session</h3><div class="icon" role="img" aria-label="Cat line icon"></div>
    <ul style="color:var(--accent)">
      <li><span>Pet Shower</span><svg width="14" height="14"><use href="#tick"/></svg></li>
      <li><span>Fitness Checkup</span><svg width="14" height="14"><use href="#tick"/></svg></li>
      <li><span>Pet Grooming</span><svg width="14" height="14"><use href="#tick"/></svg></li>
      <li><span>Hair And Nail Cut</span><svg width="14" height="14"><use href="#tick"/></svg></li>
      <li><span>Control Hair Falling</span><svg width="14" height="14" style="color:var(--green)"><use href="#cross"/></svg></li>
      <li><span>Brush &amp; Blow Dry</span><svg width="14" height="14" style="color:var(--green)"><use href="#cross"/></svg></li>
      <li><span>Pet Park And Games</span><svg width="14" height="14" style="color:var(--green)"><use href="#cross"/></svg></li>
    </ul>
    <p class="price">$150 <small>/ Per Session</small></p>
  </article>
</section>

<section class="abs gallery">
  <div role="img" aria-label="Tabby cat eating from a hand" style="background:linear-gradient(135deg,#8a6a4e,#d9cbbb)"></div>
  <div role="img" aria-label="Grey tabby cat close-up" style="background:linear-gradient(135deg,#7d7d7a,#c6c5c0)"></div>
  <div role="img" aria-label="Woman holding a white cat" style="background:linear-gradient(135deg,#c9a46e,#3b302a)"></div>
  <div role="img" aria-label="Tabby cat resting" style="background:linear-gradient(135deg,#a88663,#4d3d2f)"></div>
  <div role="img" aria-label="Man smiling with a ginger cat" style="background:linear-gradient(135deg,#e8e4de,#c48a5a)"></div>
</section>

<section class="testimonials">
  <p class="abs eyebrow center" style="top:3534px">Clients Testimonials</p>
  <h2 class="abs section-title center" style="top:3572px">Amazing Clients Feedback</h2>
  <div class="abs avatar" role="img" aria-label="Client portrait with her cat"></div>
  <p class="abs center" style="top:3777px;font-size:16px;font-weight:700">Mara Ellison</p>
  <p class="abs center" style="top:3803px;font-size:12px;color:var(--muted)">Pet Lover</p>
  <p class="abs center" style="top:3848px;left:225px;width:750px;font-size:14px;line-height:24px;color:var(--text)">Lorem ipsum dolor sit amet, consectetur adipiscing elit. Quisque non nulla eu elit maximus tempus molestie sit amet libero. Sed erat massa, ornare ac orci ut, faucibus convallis turpis. Sed aliquam, lorem ut faucibus placerat, magna sapien convallis tellus, sit amet consequat ante sem vel urna.</p>
  <div class="abs dots"><i class="on"></i><i></i><i></i></div>
</section>

<section class="abs newsletter">
  <h2>Newsletter Sign Up</h2>
  <p>We will contact you as soon as possible</p>
  <div class="news-input">Enter your email<span class="go"><svg width="22" height="14" viewBox="0 0 22 14"><path d="M1 7h19M14 1l6 6-6 6" fill="none" stroke="#fff" stroke-width="1.6"/></svg></span></div>
</section>

<footer>
  <div class="abs foot-brand"><div class="brand-mark"></div><div class="brand-name" style="font-size:22px;line-height:24px">Honey Paws<br>Cat Sitting</div></div>
  <div class="abs foot-col" style="left:350px;top:4418px">
    <h4>Service Areas</h4>
    <ul>
      <li><svg width="12" height="16" viewBox="0 0 12 16"><path d="M6 0a6 6 0 0 1 6 6c0 4-6 10-6 10S0 10 0 6a6 6 0 0 1 6-6z" fill="var(--green)"/><circle cx="6" cy="6" r="2.2" fill="#fff"/></svg>Lorem Ipsum</li>
      <li><svg width="12" height="16" viewBox="0 0 12 16"><path d="M6 0a6 6 0 0 1 6 6c0 4-6 10-6 10S0 10 0 6a6 6 0 0 1 6-6z" fill="var(--green)"/><circle cx="6" cy="6" r="2.2" fill="#fff"/></svg>Lorem Ipsum</li>
      <li><svg width="12" height="16" viewBox="0 0 12 16"><path d="M6 0a6 6 0 0 1 6 6c0 4-6 10-6 10S0 10 0 6a6 6 0 0 1 6-6z" fill="var(--green)"/><circle cx="6" cy="6" r="2.2" fill="#fff"/></svg>Lorem Ipsum</li>
      <li><svg width="12" height="16" viewBox="0 0 12 16"><path d="M6 0a6 6 0 0 1 6 6c0 4-6 10-6 10S0 10 0 6a6 6 0 0 1 6-6z" fill="var(--green)"/><circle cx="6" cy="6" r="2.2" fill="#fff"/></svg>Lorem Ipsum</li>
      <li><svg width="12" height="16" viewBox="0 0 12 16"><path d="M6 0a6 6 0 0 1 6 6c0 4-6 10-6 10S0 10 0 6a6 6 0 0 1 6-6z" fill="var(--green)"/><circle cx="6" cy="6" r="2.2" fill="#fff"/></svg>Lorem Ipsum</li>
    </ul>
  </div>
  <div class="abs foot-col" style="left:552px;top:4418px;width:280px">
    <h4>Hours of Operation</h4>
    <p>My support available to help you 24 hours a day. We provide our best.</p>
    <p style="margin-top:8px">Mon – Fri : 08.00 am – 20.00 pm</p>
    <p>Saturday : 09.00 am – 20.00 pm</p>
    <p>Sunday : We Are Closed</p>
  </div>
  <div class="abs foot-col" style="left:882px;top:4418px">
    <h4>Contact Info</h4>
    <ul>
      <li><svg width="14" height="14" viewBox="0 0 24 24"><path d="M5 3h4l2 5-2.5 1.5a11 11 0 0 0 6 6L16 13l5 2v4a2 2 0 0 1-2 2A16 16 0 0 1 3 5a2 2 0 0 1 2-2z" fill="var(--green)"/></svg>415-555-0192</li>
      <li><svg width="14" height="12" viewBox="0 0 14 12"><rect width="14" height="12" rx="1" fill="var(--green)"/><path d="M1 2l6 4 6-4" fill="none" stroke="#fff" stroke-width="1.2"/></svg>hello@honeypawscatsitting.com</li>
      <li><svg width="14" height="14" viewBox="0 0 14 14"><circle cx="7" cy="7" r="6.3" fill="none" stroke="var(--green)" stroke-width="1.3"/><path d="M1 7h12M7 1c-3 3-3 9 0 12M7 1c3 3 3 9 0 12" fill="none" stroke="var(--green)" stroke-width="1"/></svg>www.honeypawscatsitting.com</li>
    </ul>
  </div>
  <div class="abs bottom">
    <span>Privacy Policy &nbsp;|&nbsp; Terms of Use</span>
    <span>© Honey Paws Cat Sitting 2022 | All Right Reserved</span>
    <span class="social"><span>FB</span><span>TW</span><span>IN</span></span>
  </div>
</footer>

</body>
</html>
```